Bookmark Design

We would like to design a book mark with logos of our two business and a quote.

One side with the quote "The first wealth is health" - Gilbert Lyle Stanton and the two logos.

The back side has the two logos with its respective phone numbers and a common address (this is to be advised to the winner of the project).

```html
<!DOCTYPE html>
<html lang="en">
<head>
<meta charset="utf-8">
<title>Bookmark – Front and Back</title>
<link rel="stylesheet" href="https://fonts.googleapis.com/css2?family=Bebas+Neue&family=Montserrat:wght@700&family=Roboto:wght@400&family=Roboto+Condensed:wght@700&display=swap">
<style>
  :root {
    --leaf-green: #8bc43f;
    --soft-green: #6ab462;
    --pale-green: #c9e4a4;
    --brand-blue: #0a4fa0;
    --paper: #ffffff;
    --page: #ffffff;
  }
  html, body {
    margin: 0;
    padding: 0;
    width: 1200px;
    height: 1200px;
    overflow: hidden;
    background: var(--page);
  }
  .canvas {
    position: relative;
    width: 1200px;
    height: 1200px;
  }
  .bookmark {
    position: absolute;
    top: 141px;
    width: 236px;
    height: 943px;
    background: var(--paper);
    overflow: hidden;
    box-shadow: 0 1px 5px rgba(0, 0, 0, 0.28);
  }
  .bookmark--front { left: 295px; }
  .bookmark--back  { left: 611px; }
  .bookmark__bg {
    position: absolute;
    inset: 0;
    width: 236px;
    height: 943px;
  }

  /* Front: quote */
  .quote {
    position: absolute;
    left: calc(118px - 300px);
    top: calc(302px - 100px);
    width: 600px;
    height: 200px;
    margin: 0;
    transform: rotate(-90deg);
    font-family: "Bebas Neue", "Oswald", sans-serif;
    font-size: 88px;
    line-height: 98px;
    letter-spacing: 0.5px;
    color: var(--brand-blue);
    text-align: center;
    text-transform: uppercase;
    font-weight: 400;
  }
  .quote__line { display: block; }
  .quote__author {
    position: absolute;
    width: 1px;
    height: 1px;
    overflow: hidden;
    clip: rect(0 0 0 0);
  }

  .foliage {
    position: absolute;
    border-radius: 60% 0 0 60%;
  }
  .foliage--top {
    right: 0;
    top: 0;
    width: 45px;
    height: 150px;
    background: linear-gradient(180deg, rgba(106, 180, 98, 0.95), rgba(106, 180, 98, 0.6));
  }
  .foliage--low {
    right: 0;
    top: 526px;
    width: 70px;
    height: 96px;
    background: linear-gradient(160deg, rgba(90, 150, 110, 0.6), rgba(201, 228, 164, 0.75));
  }

  /* Brand name blocks */
  .brand {
    position: absolute;
    left: 0;
    width: 236px;
    display: flex;
    flex-direction: column;
    align-items: center;
    font-family: "Montserrat", sans-serif;
    font-weight: 700;
  }
  .brand__mark {
    width: 90px;
    height: 90px;
    border-radius: 50%;
    border: 3px solid var(--brand-blue);
    box-sizing: border-box;
    margin-bottom: 16px;
  }
  .brand__name {
    margin: 0;
    text-align: center;
    line-height: 1.1;
  }
  .brand--clinic .brand__name {
    color: var(--brand-blue);
    font-size: 22px;
    letter-spacing: 0.5px;
  }
  .brand--dental {
    flex-direction: row;
    justify-content: center;
    gap: 10px;
  }
  .brand__square {
    width: 30px;
    height: 30px;
    background: var(--soft-green);
    flex: none;
  }
  .brand--dental .brand__name {
    color: var(--soft-green);
    font-size: 27px;
    letter-spacing: 0.5px;
    text-align: left;
    line-height: 1.15;
  }

  .bookmark--front .brand--clinic { top: 632px; }
  .bookmark--front .brand--dental { top: 828px; }
  .bookmark--back  .brand--clinic { top: 49px; }
  .bookmark--back  .brand--dental { top: 255px; }

  /* Back: contact */
  .contact {
    position: absolute;
    left: 0;
    top: 461px;
    width: 236px;
    display: flex;
    flex-direction: column;
    align-items: center;
    color: var(--paper);
  }
  .contact__icon { display: block; }
  .contact__address {
    margin: 10px 0 0;
    font-family: "Roboto", Arial, sans-serif;
    font-size: 14px;
    line-height: 18px;
    text-align: center;
    font-style: normal;
  }
  .contact__phone-icon { margin-top: 22px; }
  .contact__phone {
    margin: 6px 0 0;
    font-family: "Roboto Condensed", Arial, sans-serif;
    font-weight: 700;
    font-size: 23px;
    letter-spacing: 0.2px;
  }

  .sprout {
    position: absolute;
    left: 0;
    right: 0;
    bottom: 0;
    height: 265px;
    border-radius: 50% 50% 0 0 / 40% 40% 0 0;
    background:
      radial-gradient(ellipse at 55% 35%, rgba(10, 79, 160, 0.55), rgba(10, 79, 160, 0) 45%),
      linear-gradient(180deg, rgba(255, 255, 255, 0.55), rgba(255, 255, 255, 0.85));
  }
</style>
</head>
<body>
<main class="canvas">

  <!-- Front side -->
  <section class="bookmark bookmark--front" aria-label="Bookmark front">
    <svg class="bookmark__bg" viewBox="0 0 236 943" aria-hidden="true">
      <rect width="236" height="943" fill="var(--paper)"/>
      <path d="M0 0 H236 V622 C190 606 150 598 110 599 C70 601 35 610 0 625 Z" fill="var(--brand-blue)"/>
      <path d="M0 0 H236 V614 C190 600 150 592 110 593 C70 595 35 603 0 614 Z" fill="var(--leaf-green)"/>
    </svg>

    <div class="foliage foliage--top" role="img" aria-label="Soft leaf decoration"></div>
    <div class="foliage foliage--low" role="img" aria-label="Small sprig of leaves"></div>

    <blockquote class="quote">
      <span class="quote__line">The first wealth</span>
      <span class="quote__line">is health</span>
      <cite class="quote__author">Gilbert Lyle Stanton</cite>
    </blockquote>

    <div class="brand brand--clinic">
      <span class="brand__mark" aria-hidden="true"></span>
      <p class="brand__name">HARLOW CLINIC</p>
    </div>
    <div class="brand brand--dental">
      <span class="brand__square" aria-hidden="true"></span>
      <p class="brand__name">BAYSIDE<br>DENTAL</p>
    </div>
  </section>

  <!-- Back side -->
  <section class="bookmark bookmark--back" aria-label="Bookmark back">
    <svg class="bookmark__bg" viewBox="0 0 236 943" aria-hidden="true">
      <rect width="236" height="943" fill="var(--paper)"/>
      <path d="M0 399 C40 397 80 396 120 397 C160 399 200 404 236 410 V943 H0 Z" fill="var(--brand-blue)"/>
      <path d="M0 411 C40 404 80 402 120 403 C160 405 200 408 236 412 V943 H0 Z" fill="var(--leaf-green)"/>
    </svg>

    <div class="brand brand--clinic">
      <span class="brand__mark" aria-hidden="true"></span>
      <p class="brand__name">HARLOW CLINIC</p>
    </div>
    <div class="brand brand--dental">
      <span class="brand__square" aria-hidden="true"></span>
      <p class="brand__name">BAYSIDE<br>DENTAL</p>
    </div>

    <div class="contact">
      <svg class="contact__icon" width="24" height="35" viewBox="0 0 24 35" aria-hidden="true">
        <path d="M12 1 C5.9 1 1 5.9 1 12 C1 19 12 34 12 34 C12 34 23 19 23 12 C23 5.9 18.1 1 12 1 Z" fill="var(--brand-blue)"/>
        <circle cx="12" cy="11.5" r="5" fill="none" stroke="var(--leaf-green)" stroke-width="2.2"/>
      </svg>
      <address class="contact__address">14 Marlow Lane,<br>Brookfield, NY</address>
      <svg class="contact__icon contact__phone-icon" width="29" height="29" viewBox="0 0 29 29" aria-hidden="true">
        <circle cx="14.5" cy="14.5" r="14.5" fill="var(--brand-blue)"/>
        <path d="M10.2 8.3 L12.4 8 L13.6 11.2 L12.3 12.5 C13 14.2 14.5 15.8 16.3 16.6 L17.6 15.3 L20.8 16.5 L20.5 18.8 C20.3 19.7 19.5 20.2 18.6 20.1 C13.2 19.5 9 15.3 8.5 10 C8.4 9.1 9.1 8.4 10.2 8.3 Z" fill="var(--leaf-green)"/>
      </svg>
      <p class="contact__phone">00 321 456 789</p>
    </div>

    <div class="sprout" role="img" aria-label="Large sprouting plant with white and blue leaves"></div>
  </section>

</main>
</body>
</html>
```